Piano genealogy graphs template, for a large poster printing

Hello and thank you for your interest in my project.
I need a poster template, so I can create structures similar to the one I have uploaded. I want to completely replace or improve my poor previous design which is attached.
I need to be able to input names and dates into boxes of various colors, arrows pointing between boxes. I would also like to be able to label each graph (not each box).
I am looking at something that would be legible when printed, in a one consistent professional layout of 2A0 (around 1189x1682 mm) poster (I know it is large). The design template required here can include just few sample text boxes with sample flags on a suitable background, for me to multiply later and spread across the whole poster.
The positioning of the boxes is not important.
Please let me know if more clarification is required.
Thank you for your help.

Feel free to follow what I have attached in the file, or change the design completely.

UPDATE 4/12: I have uploaded two more graphs as an example. At this stage of the contest, I would like to have one of those graphs done, and I am planning to offer a 'freelance job' to one or two designers, who will be willing to do the whole 10 graphs on one poster.

Reason: Dear Designers, Since the project is rather complex and large-scale, I have decided to give everyone more time to work on their designs. I will consider extending it further if any of you require additional time. Best wishes, leopold

Dear Designers, I would like to inform you that the contest for my poster is now closed and that I have assigned the prizes. I would like to thank all of you for submiting your high-quality designs, and for your participation. It was a great pleasure working with all of you. Due to the large size of the project itself (large number of graphs to be fitted on a single poster), I had to focus on providing feedback to only those designers who provided projects closest to what I was expecting at the early stages of the contest. I wish you all the best for the future, Kind regards, Leopold

Target Market(s)

Pianists, historians

Industry/Entity Type

Printing

Requirements
Must have
• Consistent design, but allow to clearly delineate various genealogy trees.

```html
<!DOCTYPE html>
<html lang="en">
<head>
<meta charset="utf-8">
<title>Piano Genealogy Poster – Branch III</title>
<link href="https://fonts.googleapis.com/css2?family=Lato:wght@400;700&display=swap" rel="stylesheet">
<style>
  :root{
    --maroon:#7e1834;
    --rose:#b47b6c;
    --cream-bg:#f3ead0;
    --box:#f2eccd;
    --box-edge:#e0cfa6;
    --root-top:#d9b48f;
    --line:#e3c59c;
    --ink:#1c1a18;
    --poland-red:#dc1c2e;
    --usa-red:#c8102e;
    --usa-blue:#1f2f6e;
    --fr-blue:#1b2a6b;
    --hu-green:#3f9a4a;
    --de-gold:#f5c400;
    --fi-blue:#0a3a8c;
  }
  *{box-sizing:border-box;margin:0;padding:0}
  html,body{width:1012px;height:1200px;overflow:hidden;background:#fff}
  body{font-family:'Lato',sans-serif;color:var(--ink);position:relative}
  .poster-field{
    position:absolute;left:0;top:0;width:1012px;height:938px;
    background:linear-gradient(to bottom,var(--maroon) 0%,var(--rose) 50%,var(--cream-bg) 100%);
  }
  .graph-title{
    position:absolute;left:54px;top:22px;width:902px;height:43px;
    background:var(--box);text-align:center;
    font-size:35px;line-height:43px;font-weight:400;
  }
  .connectors{position:absolute;left:0;top:0}
  .person{
    position:absolute;
    filter:drop-shadow(3px 4px 3px rgba(60,20,20,.45));
  }
  .person .card{
    width:100%;height:100%;
    background:var(--box);
    border:2px solid var(--box-edge);
    padding:6px 10px 0 18px;
    font-size:17px;line-height:1.15;
    clip-path:polygon(0 0,calc(100% - 26px) 0,100% 26px,100% 100%,0 100%);
  }
  .person.mirror .card{
    clip-path:polygon(26px 0,100% 0,100% 100%,0 100%,0 26px);
    padding-left:22px;
  }
  .person.root .card{background:linear-gradient(to bottom,var(--root-top),var(--box))}
  .name{display:block;padding-left:8px}
  .dates{display:flex;align-items:center;gap:4px;margin-top:7px}
  .label{display:block;margin-top:6px}
  .flag{display:inline-block;width:38px;height:23px;flex:none}
  .flag-pl{background:linear-gradient(#fff 50%,var(--poland-red) 50%)}
  .flag-hu{background:linear-gradient(var(--poland-red) 33.3%,#fff 33.3% 66.6%,var(--hu-green) 66.6%)}
  .flag-de{background:linear-gradient(#000 33.3%,var(--poland-red) 33.3% 66.6%,var(--de-gold) 66.6%)}
  .flag-fr{background:linear-gradient(to right,var(--fr-blue) 33.3%,#fff 33.3% 66.6%,var(--poland-red) 66.6%)}
  .flag-fi{background:
    linear-gradient(to right,transparent 28%,var(--fi-blue) 28% 44%,transparent 44%),
    linear-gradient(transparent 38%,var(--fi-blue) 38% 62%,transparent 62%),#fff}
  .flag-us{position:relative;background:repeating-linear-gradient(var(--usa-red) 0 1.77px,#fff 1.77px 3.54px)}
  .flag-us::before{content:"";position:absolute;left:0;top:0;width:42%;height:54%;background:var(--usa-blue)}
  .spec-note{
    position:absolute;left:96px;top:1028px;
    font-size:97px;font-weight:400;line-height:1;letter-spacing:.5px;
  }
</style>
</head>
<body>
  <main class="poster-field">
    <svg class="connectors" width="1012" height="938" viewBox="0 0 1265 1172" fill="none" stroke="var(--line)" stroke-width="5">
      <defs>
        <marker id="tip" viewBox="0 0 10 10" refX="8" refY="5" markerWidth="4" markerHeight="4" orient="auto">
          <path d="M0 0 L10 5 L0 10 Z" fill="var(--line)" stroke="none"/>
        </marker>
      </defs>
      <path d="M50 185 V665"/>
      <path d="M50 250 H144" marker-end="url(#tip)"/>
      <path d="M50 665 H144" marker-end="url(#tip)"/>
      <path d="M150 285 V560"/>
      <path d="M150 352 H246" marker-end="url(#tip)"/>
      <path d="M150 560 H246" marker-end="url(#tip)"/>
      <path d="M255 390 V455 H349" marker-end="url(#tip)"/>
      <path d="M150 704 V745 H246" marker-end="url(#tip)"/>
      <path d="M255 848 V935 H349" marker-end="url(#tip)" opacity=".55"/>
      <path d="M1215 185 V392"/>
      <path d="M1215 240 H1124" marker-end="url(#tip)"/>
      <path d="M1215 392 H1124" marker-end="url(#tip)"/>
      <path d="M1116 285 V352 H1022" marker-end="url(#tip)"/>
      <path d="M1116 495 V562 H1022" marker-end="url(#tip)"/>
    </svg>

    <h1 class="graph-title">American Tree, Branch III - Orlik and Halasz</h1>

    <div class="person root" style="left:38px;top:92px;width:178px;height:56px">
      <div class="card" style="padding-left:10px"><span class="name">Tadeusz Orlik</span>
        <span class="dates" style="margin-top:4px">(1810-1849) <i class="flag flag-pl"></i></span></div>
    </div>
    <div class="person" style="left:120px;top:172px;width:180px;height:56px">
      <div class="card"><span class="name" style="padding-left:20px">Karl Weronik</span>
        <span class="dates" style="margin-top:4px">(1819-1897) <i class="flag flag-pl"></i></span></div>
    </div>
    <div class="person" style="left:202px;top:250px;width:190px;height:62px">
      <div class="card"><span class="name">Moriz Lindqvist</span>
        <span class="dates">(1862-1946) <i class="flag flag-pl"></i></span></div>
    </div>
    <div class="person" style="left:284px;top:334px;width:174px;height:61px">
      <div class="card"><span class="name">Charles Barlow</span>
        <span class="dates">(1927-2012) <i class="flag flag-us"></i></span></div>
    </div>
    <div class="person" style="left:202px;top:418px;width:236px;height:61px">
      <div class="card"><span class="name" style="padding-left:0">Mieczyslaw Zabrowski</span>
        <span class="dates">(1892-1993) <i class="flag flag-pl"></i><i class="flag flag-us"></i></span></div>
    </div>
    <div class="person" style="left:120px;top:502px;width:186px;height:61px">
      <div class="card"><span class="name">Georges Lamotte</span>
        <span class="dates" style="margin-top:4px">(1826-1910) <i class="flag flag-fr" style="width:32px"></i></span></div>
    </div>
    <div class="person" style="left:202px;top:586px;width:208px;height:60px">
      <div class="card"><span class="name" style="padding-left:22px">Isidore Vasary</span>
        <span class="dates">(1863-1958) <i class="flag flag-hu"></i><i class="flag flag-fr" style="width:32px"></i></span></div>
    </div>
    <div class="person" style="left:284px;top:700px;width:190px;height:196px">
      <div class="card" style="padding-left:14px"><span class="name" style="padding-left:0">Beveridge Hollis</span>
        <span class="dates">(1908-1999) <i class="flag flag-us"></i></span>
        <span class="label">Students:<br>Matti Kaartinen</span>
        <span class="dates">(1954) <i class="flag flag-fi"></i><i class="flag flag-us"></i></span>
        <span class="label" style="margin-top:9px">Robert Fairlane</span>
        <span class="dates" style="margin-top:2px"><i class="flag flag-us"></i></span></div>
    </div>

    <div class="person root mirror" style="left:790px;top:92px;width:184px;height:56px">
      <div class="card"><span class="name" style="padding-left:42px">Ferenc Halasz</span>
        <span class="dates" style="margin-top:4px">(1811-1886) <i class="flag flag-hu" style="width:33px"></i></span></div>
    </div>
    <div class="person mirror" style="left:714px;top:168px;width:179px;height:60px">
      <div class="card"><span class="name">Emil von Reuter</span>
        <span class="dates">(1862-1942) <i class="flag flag-de" style="width:33px"></i></span></div>
    </div>
    <div class="person mirror" style="left:636px;top:250px;width:176px;height:62px">
      <div class="card" style="padding-left:18px"><span class="name" style="padding-left:42px">Earl Brandt</span>
        <span class="dates">(1915-2010) <i class="flag flag-us"></i></span></div>
    </div>
    <div class="person mirror" style="left:718px;top:336px;width:175px;height:60px">
      <div class="card"><span class="name">Moriz Lindqvist</span>
        <span class="dates">(1862-1946) <i class="flag flag-pl" style="width:33px"></i></span></div>
    </div>
    <div class="person mirror" style="left:638px;top:418px;width:174px;height:61px">
      <div class="card" style="padding-left:18px"><span class="name" style="padding-left:22px">Charles Barlow</span>
        <span class="dates">(1927-2012) <i class="flag flag-us"></i></span></div>
    </div>
  </main>

  <p class="spec-note">Font 36pt i 18pt</p>
</body>
</html>
```